Postcard Design

We need a postcard designed for our company Vorta-Bin. Vorta-bin specializes in providing a tailored document destruction service that allows businesses to comply with legislation and ensure that the client, employee and confidential business information is kept secure at all times. We would like to see a postcard with greys, blues, blacks, and whites in it. I have attached a few logos for your reference. I would like the front of the postcard to be a picture design only with our company logo info. The back should have a message that says:

Dear Valued Customer,
We are sending you this letter because you currently utilize our On-site paper destruction service. We want to make you aware of our Plant-Based paper destruction service and the benefits to you and to the environment. Currently, 60% of our customers receive, and are highly satisfied with our Plant-Based Service.

Definitions:
On-site Service – Customer’s material is destroyed at the Customer’s location
Plant-Based Service – Customer’s material is destroyed at a Vorta-bin Secured Facility

What Would Not Change:

Security:
- All trucks are equipped with GPS tracking devices
- Our facility is monitored by CCTV 24 hours a day 7 days a week
- Our box trucks are equipped with secure alarm systems
- Annual Background Checks and Drug Screens are ran on all employees

Plant-Based Service Benefits:
- Less Noise at your Location
- Less Time in your Parking Lot
- Reduced Fuel Consumption
- Environmentally Friendly
- Flexibility
- Quicker turn-around times on all Service Requests (i.e., Purges / Earlier Pick-Ups)

We will begin changing your service from On-site to Plant Based starting August 1st. The process will take an additional 60 days to fully implement so you may not see a change right away. Our On-site capabilities are NOT going away. If you wish to remain an On-site customer all you have to do is call or email me your request. I am also available should you have any questions. My contact information is below.
We appreciate your consideration in regards to this matter and, as always, thank you for your business.

Marcus T. Elwin
General Manager
Marcus.Elwin@vortabin-example.com
408.617.5530

is there enough room to get this on the back of the card?

```html
<!DOCTYPE html>
<html lang="en">
<head>
<meta charset="utf-8">
<title>Vorta-Bin Postcard – Back</title>
<link href="https://fonts.googleapis.com/css2?family=Roboto+Condensed:wght@300;400;700&display=swap" rel="stylesheet">
<style>
  :root {
    --ink: #2f2f33;
    --navy: #1c4f8f;
    --navy-deep: #0e3f7c;
    --band-dark: #0b4282;
    --band-mid: #1668ae;
    --paper-top: #eef5fb;
    --paper-bottom: #ffffff;
    --white: #ffffff;
    --truck-body: #e6e9ee;
    --truck-shade: #9aa3ae;
  }
  html, body {
    margin: 0;
    padding: 0;
    overflow: hidden;
  }
  body {
    width: 1200px;
    height: 930px;
    font-family: "Roboto Condensed", "Arial Narrow", sans-serif;
  }
  .postcard {
    position: relative;
    width: 1200px;
    height: 930px;
    overflow: hidden;
    background: linear-gradient(180deg, var(--paper-top) 0%, var(--paper-bottom) 45%, var(--paper-top) 100%);
    color: var(--ink);
    font-weight: 300;
    font-size: 24px;
    line-height: 30px;
  }
  .block {
    position: absolute;
    left: 44px;
    margin: 0;
  }
  .heading {
    color: var(--navy);
    font-weight: 700;
    font-size: 24px;
    margin: 0;
  }
  .intro { top: 38px; width: 1120px; }
  .intro p, .definitions p { margin: 0; }
  .definitions { top: 182px; width: 880px; }
  .unchanged-title { top: 296px; }
  .truck {
    position: absolute;
    left: 955px;
    top: 240px;
    width: 205px;
    height: 100px;
  }
  .feature-band {
    position: absolute;
    left: 0;
    top: 342px;
    width: 1200px;
    height: 280px;
    background: linear-gradient(90deg, var(--band-dark) 0%, var(--band-mid) 55%, var(--band-dark) 100%);
    color: var(--white);
  }
  .feature-column {
    position: absolute;
    top: 12px;
  }
  .feature-column.security { left: 44px; width: 550px; }
  .feature-column.benefits { left: 638px; width: 530px; }
  .feature-column h2 {
    margin: 0 0 2px;
    font-size: 24px;
    font-weight: 700;
    line-height: 30px;
  }
  .feature-list {
    list-style: none;
    margin: 0;
    padding: 0;
    font-size: 25px;
    line-height: 32px;
  }
  .feature-list li {
    position: relative;
    padding-left: 31px;
  }
  .feature-list li::before {
    content: "✓";
    position: absolute;
    left: 0;
    top: 0;
  }
  .closing { top: 647px; width: 1120px; }
  .closing p { margin: 0 0 24px; }
  .signature {
    position: absolute;
    left: 36px;
    top: 858px;
    margin: 0;
    color: var(--navy-deep);
    font-weight: 700;
    font-size: 31px;
    line-height: 38px;
    white-space: nowrap;
  }
  .signature .sep { padding: 0 10px; }
</style>
</head>
<body>
<main class="postcard">
  <section class="block intro">
    <h1 class="heading">Dear Valued Customer,</h1>
    <p>We are sending you this letter because you currently utilize our On-site paper destruction service. We want to make you aware of our Plant-Based paper destruction service and the benefits to you and to the environment. Currently, 60% of our customers receive, and are highly satisfied with our Plant-Based Service.</p>
  </section>

  <section class="block definitions">
    <h2 class="heading">Definitions:</h2>
    <p>On-site Service – Customer’s material is destroyed at the Customer’s location</p>
    <p>Plant-Based Service – Customer’s material is destroyed at a Vorta-bin Secured Facility</p>
  </section>

  <h2 class="block heading unchanged-title">What Would Not Change:</h2>

  <svg class="truck" viewBox="0 0 205 100" role="img" aria-label="Illustration of a company box truck">
    <rect x="0" y="0" width="205" height="100" rx="6" fill="var(--truck-body)"/>
    <rect x="0" y="78" width="205" height="22" rx="6" fill="var(--truck-shade)" opacity="0.5"/>
  </svg>

  <section class="feature-band">
    <div class="feature-column security">
      <h2>Security:</h2>
      <ul class="feature-list">
        <li>All trucks are equipped with GPS tracking devices</li>
        <li>Our facility is monitored by CCTV 24 hours a<br>day 7 days a week</li>
        <li>Our box trucks are equipped with secure<br>alarm systems</li>
        <li>Annual Background Checks and Drug Screens are ran<br>on all employees</li>
      </ul>
    </div>
    <div class="feature-column benefits">
      <h2>Plant-Based Service Benefits:</h2>
      <ul class="feature-list">
        <li>Less Noise at your Location</li>
        <li>Less Time in your Parking Lot</li>
        <li>Reduced Fuel Consumption</li>
        <li>Environmentally Friendly</li>
        <li>Flexibility</li>
        <li>Quicker turn-around times on all Service<br>Requests (i.e., Purges / Earlier Pick-Ups)</li>
      </ul>
    </div>
  </section>

  <section class="block closing">
    <p>We will begin changing your service from On-site to Plant Based starting August 1st. The process will take an additional 60 days to fully implement so you may not see a change right away. Our On-site capabilities are NOT going away. If you wish to remain an On-site customer all you have to do is call or email me your request. I am also available should you have any questions. My contact information is below.</p>
    <p>We appreciate your consideration in regards to this matter and, as always, thank you for your business.</p>
  </section>

  <p class="signature">Marcus T. Elwin<span class="sep">|</span>General Manager<span class="sep">|</span>Marcus.Elwin@vortabin-example.com<span class="sep">|</span>408.617.5530</p>
</main>
</body>
</html>
```